Dapple Brew, a new venture, serving our customers at functions and events, lovingly made coffee fro

www.dapplebrew.com.au

Dapple Brew Wordpress

The font type of our logo is: La Chatte à Maman (it can be downloaded in dafont.com)

Our trading name is Dapple Brew. We have a passion for well made coffee and providing service with affection.

Our new logo design is being placed on the side and rear of our restored 1976 Kombi. I have attached our logo and a picture of our van. We would like to own the rights to all work on our site, with access to make additions and amendments as required with no restrictions.

We want our event business to grow through our branding of great service and lovingly made coffee.

We would like our WordPress design to be simple with a retro image that our 76 Kombi portrays as well as the hipster coffee culture of Melbourne.

To begin with we are thinking of 5 pages but are open to any suggestions you think would benefit our development. We would also like to have links to our new Brewbook and Instagram pages on the bottom of each page.

Logo -Like us on Brewbook
https://www.facebook.com/pages/Dapple-Brew/5820371946618405

Logo -follow us on Instagram
Dapple_brew

Home

Beautifully made coffee is a pleasure we should all enjoy at least once in our day.
Served from our restored 1976 Kombi we strive to provide you with an experience that will enhance your day. The care we show comes from years of training and experience as a Battista in several countries around the world.
We trust the joy of our lovingly made coffee and our retro style service will linger.
Serving great coffee at an event or function near you
Dapple Brew.

About
Dapple brew believes in good old fashion retro service and a high a quality product. We care that our customers receive a beautifully made coffee, chai or hot chocolate. We serve our patrons with a heartfelt smile, aiming to enhance their day.
We are fortunate enough to operate from our recently restored 1976 Kombi at functions and events around Melbourne.
You can follow us on Brewbook and Instagram or book us for you special function via our contact page.
We look forward to wing able to serve you.
Dapple Brew.

Contact Us - Safe and secure

To book us at your special function, please fill in your details below and we will respond to your query as soon as possible.

Name:

Company name:

Phone number:

Email address:

Question or comment: ( box )

Dapple Brew
Melbourne, Victoria, Australia
Info@dapplebrew.com.au
0471 925 164
Operating at your local function or event

Blog
Brewbook and Instagram integration.

Links

We have a heartfelt passionate and eternal pursuit for exceeding expectations, providing a memorable experience. It follows that we align ourselves with organizations, business's and people who also strive for perfection in what they do, providing great services, products and customer care.

Feel free to contact some of our contacts below who we have found to be above and beyond.

The Tamper Mill group - equipment suppliers

http://www.grindworks-supply.com.au

Kesi- barista consulting services

https://www.facebook.com/pages/Prime...Kesi/7301958264417086

Reedfinch Swimming Club

http://reedfinch.com.au/

Wexmoor Baseball Club

www.wexmoorfalcons.com.au/

Pellby Autos

http://www.pellbyautos.com.au

Target Market(s)

Lovers of Coffee at events and functions. Customers wanting coffee catered for at their event of function

Industry/Entity Type

Cafe

Font styles to use
Other font styles liked:
• La Chatte à Maman

Requirements
Must have
• Our logo design
• 5 pages but are open to any suggestions you think would benefit our development. We would also like to have links to our new Brewbook and Instagram pages on the bottom of each page.
Nice to have
• Your artistic flair and input

```html
<!DOCTYPE html>
<html lang="en">
<head>
<meta charset="utf-8">
<title>Dapple Brew – Hot Coffee Theme</title>
<link href="https://fonts.googleapis.com/css2?family=Open+Sans:wght@400;600;700&family=Lobster&display=swap" rel="stylesheet">
<style>
:root{
  --black:#111010;
  --gold:#b8925a;
  --gold-light:#d2b27c;
  --gold-dark:#8c6a3a;
  --maroon:#3a0a07;
  --maroon-card:#3b100b;
  --bean:#6e3f3a;
  --footer:#3c3e3d;
  --white:#ffffff;
  --ink:#2a1a10;
  --grey:#888;
}
*{margin:0;padding:0;box-sizing:border-box}
html,body{width:1200px;height:3102px;overflow:hidden;background:var(--white)}
body{position:relative;font-family:"Open Sans",Arial,sans-serif;color:var(--ink)}
.abs{position:absolute}
.script{font-family:"Lobster",cursive;font-weight:400}

/* nav */
.site-nav{left:0;top:0;width:1200px;height:112px;background:var(--black);border-bottom:4px solid var(--gold)}
.brand{left:30px;top:22px;width:150px;height:150px;border-radius:50%;background:var(--black);color:var(--white);font-size:26px;font-weight:700;display:flex;align-items:center;justify-content:center;text-align:center;line-height:1.1;z-index:3}
.nav-links{right:40px;top:54px;display:flex;gap:38px;list-style:none}
.nav-links li{color:var(--white);font-size:17px;font-weight:700;display:flex;align-items:center;gap:10px}
.nav-links li::before{content:"";width:11px;height:11px;background:var(--gold)}

/* hero */
.hero{left:0;top:116px;width:1200px;height:506px;background:linear-gradient(180deg,#8b8f92 0%,#a5a29a 35%,#9b3a34 60%,#5d4a3e 100%)}
.hero-title{left:260px;top:124px;width:690px;height:72px;background:rgba(30,30,30,.85);color:var(--white);font-size:50px;font-weight:700;text-align:center;line-height:72px}
.hero-sub{left:320px;top:228px;width:570px;height:48px;background:rgba(30,30,30,.8);color:var(--white);font-size:30px;font-weight:700;text-align:center;line-height:48px}
.hero-btn{left:415px;top:324px;width:370px;height:50px;border:2px solid var(--white);background:rgba(60,20,15,.6);color:var(--white);font-size:22px;font-weight:600;text-align:center;line-height:46px}
.slide-arrow{width:40px;height:40px;border-radius:50%;background:rgba(255,255,255,.4)}

/* features */
.features{left:0;top:622px;width:1200px;height:381px;background:linear-gradient(135deg,var(--gold-light),var(--gold) 55%,var(--gold-dark))}
.feature{width:300px;text-align:center}
.feature .icon{width:112px;height:112px;margin:0 auto;border-radius:50%;background:var(--white);border:6px solid var(--gold-light);display:flex;align-items:center;justify-content:center}
.feature h3{margin-top:26px;font-size:23px;font-weight:700;color:var(--ink)}
.feature p{margin-top:10px;font-size:14px;line-height:1.45;color:#3a2a18;padding:0 20px}

/* beans band */
.beans{left:0;top:1003px;width:1200px;height:361px;background:radial-gradient(ellipse at 50% 50%,#8a5a52,var(--bean) 60%,#4a2622)}
.beans-name{left:0;top:48px;width:1200px;text-align:center;color:var(--white);font-size:28px}
.beans-dot{left:593px;top:90px;width:14px;height:14px;border-radius:50%;background:var(--white)}
.beans-head{left:0;top:150px;width:1200px;text-align:center;color:var(--white);font-size:40px;font-weight:400}
.beans-btn{left:470px;top:250px;width:260px;height:44px;border:2px solid var(--white);color:var(--white);font-size:20px;text-align:center;line-height:40px}

/* gallery */
.gallery-head{left:0;top:1400px;width:1200px;text-align:center;font-size:38px;color:var(--ink)}
.gallery-head span{color:var(--gold)}
.rule{height:2px;background:#c9c9c9}
.card{top:1524px;width:280px;height:470px;border-radius:22px;overflow:hidden;background:var(--maroon-card);color:var(--white);text-align:center}
.card.alt{background:var(--gold)}
.card .photo{height:182px}
.card h4{margin-top:30px;font-size:21px;font-weight:600}
.card p{margin:12px 24px 0;font-size:14px;line-height:1.45}
.card .more{margin:26px auto 0;width:120px;height:32px;border:2px solid var(--white);border-radius:6px;background:var(--white);color:var(--ink);font-size:13px;line-height:28px}
.gal-arrow{top:1668px;width:30px;height:34px}

/* taste band */
.taste-strip{left:0;top:2026px;width:1200px;height:18px;background:var(--gold)}
.taste{left:0;top:2044px;width:1200px;height:444px;background:var(--maroon)}
.taste h2{left:0;width:1200px;text-align:center;font-size:62px;line-height:1}
.taste p{left:290px;top:244px;width:620px;text-align:center;color:var(--white);font-size:17px;line-height:1.4}
.taste-notch{left:570px;top:2026px;z-index:2}

/* order */
.order{left:289px;top:2520px;width:622px;height:136px;border-radius:16px;background:linear-gradient(90deg,#3a2418,#6b4a33 50%,#3a2418);border:2px solid #2a1a10}
.order-icon{left:72px;top:28px;width:80px;height:80px;border:3px solid var(--gold-light);border-radius:8px;display:flex;align-items:center;justify-content:center}
.order h3{left:190px;top:16px;font-size:56px;font-weight:700;color:var(--gold-light)}
.order p{left:194px;top:90px;font-size:19px;color:var(--white)}

/* footer */
.footer{left:0;top:2708px;width:1200px;height:394px;background:var(--footer);color:var(--white)}
.footer h5{font-size:19px;font-weight:700;letter-spacing:.5px}
.footer p{font-size:14px;line-height:1.6}
.foot-nav{list-style:none;font-size:14px;line-height:2}
.foot-nav li::before{content:"›";margin-right:12px;color:var(--gold-light)}
.social{list-style:none}
.social li{display:flex;align-items:center;gap:14px;font-size:14px;margin-bottom:18px}
.social li::before{content:"";width:30px;height:30px;border-radius:50%;background:var(--gold)}
.foot-brand{left:910px;top:110px;width:212px;height:120px;background:var(--white);color:var(--black);font-size:26px;font-weight:700;display:flex;align-items:center;justify-content:center}
.foot-base{left:0;top:366px;width:1200px;height:28px;background:#2e302f}
</style>
</head>
<body>

<header class="abs site-nav">
  <div class="abs brand">Dapple<br>Brew</div>
  <ul class="abs nav-links">
    <li>HOME</li><li>MENU</li><li>GALLERY</li><li>ABOUT</li><li>CONTACT</li>
  </ul>
</header>

<section class="abs hero" role="img" aria-label="Photograph of a restored red and white camper van">
  <div class="abs hero-title">HOT COFFEE THEME</div>
  <div class="abs hero-sub">GOOD WE ARE HERE TO SERVE YOU</div>
  <div class="abs hero-btn">GET STARTED</div>
  <svg class="abs slide-arrow" style="left:20px;top:236px" viewBox="0 0 40 40"><path d="M24 12 L16 20 L24 28" fill="none" stroke="#fff" stroke-width="3"/></svg>
  <svg class="abs slide-arrow" style="left:1140px;top:236px" viewBox="0 0 40 40"><path d="M16 12 L24 20 L16 28" fill="none" stroke="#fff" stroke-width="3"/></svg>
</section>

<section class="abs features">
  <div class="abs feature" style="left:107px;top:60px">
    <div class="icon"><svg width="52" height="52" viewBox="0 0 52 52"><path d="M10 20 H36 V30 A12 12 0 0 1 24 42 H22 A12 12 0 0 1 10 30 Z" fill="#2a1a10"/><path d="M36 23 H41 A5 5 0 0 1 41 33 H35" fill="none" stroke="#2a1a10" stroke-width="3"/><rect x="6" y="44" width="36" height="3" fill="#2a1a10"/></svg></div>
    <h3>GET INSPIRED</h3>
    <p>This is Pixelwright's version of Lorem Ipsum. Proin gravida nibh vel velit auctor aliquet.</p>
  </div>
  <div class="abs feature" style="left:444px;top:60px">
    <div class="icon"><svg width="52" height="52" viewBox="0 0 52 52"><path d="M26 6 A13 13 0 0 1 39 19 C39 30 26 46 26 46 C26 46 13 30 13 19 A13 13 0 0 1 26 6 Z" fill="#2a1a10"/><circle cx="26" cy="19" r="5" fill="#fff"/></svg></div>
    <h3>GET LOCATION</h3>
    <p>This is Pixelwright's version of Lorem Ipsum. Proin gravida nibh vel velit auctor aliquet.</p>
  </div>
  <div class="abs feature" style="left:785px;top:60px">
    <div class="icon"><svg width="52" height="52" viewBox="0 0 52 52"><circle cx="26" cy="18" r="9" fill="#2a1a10"/><path d="M10 44 A16 14 0 0 1 42 44 Z" fill="#2a1a10"/></svg></div>
    <h3>GET SOCIAL</h3>
    <p>This is Pixelwright's version of Lorem Ipsum. Proin gravida nibh vel velit auctor aliquet.</p>
  </div>
</section>

<section class="abs beans" role="img" aria-label="Close-up photograph of roasted coffee beans">
  <div class="abs beans-name">Dapple Brew</div>
  <div class="abs beans-dot"></div>
  <h2 class="abs beans-head">COFFEE AND LOVE ARE BEST WHEN THEY ARE HOT!</h2>
  <div class="abs beans-btn">READ MORE</div>
</section>

<h2 class="abs gallery-head script">Our <span>Gallery</span></h2>
<div class="abs rule" style="left:400px;top:1428px;width:110px"></div>
<div class="abs rule" style="left:690px;top:1428px;width:110px"></div>
<div class="abs" style="left:588px;top:1458px;width:24px;height:14px;border-radius:50%;background:var(--ink)"></div>

<svg class="abs gal-arrow" style="left:34px" viewBox="0 0 30 34"><path d="M20 6 L10 17 L20 28" fill="none" stroke="#777" stroke-width="4"/></svg>
<svg class="abs gal-arrow" style="left:1136px" viewBox="0 0 30 34"><path d="M10 6 L20 17 L10 28" fill="none" stroke="#777" stroke-width="4"/></svg>

<article class="abs card" style="left:120px">
  <div class="photo" role="img" aria-label="Photograph of a cup of coffee on a saucer" style="background:linear-gradient(160deg,#e8dcc8,#b9976a 60%,#6a4a2e)"></div>
  <h4>ELITE COFFEE</h4>
  <p>This is Pixelwright's version of Lorem Ipsum. Proin gravida nibh vel velit auctor aliquet.</p>
  <div class="more">Read More</div>
</article>
<article class="abs card alt" style="left:450px">
  <div class="photo" role="img" aria-label="Photograph of an espresso in a white cup" style="background:linear-gradient(160deg,#2a1610,#7a4a28 55%,#d9c7a8)"></div>
  <h4>ESPRESSO</h4>
  <p>This is Pixelwright's version of Lorem Ipsum. Proin gravida nibh vel velit auctor aliquet.</p>
  <div class="more">Read More</div>
</article>
<article class="abs card" style="left:778px">
  <div class="photo" role="img" aria-label="Photograph of a green latte with foam art" style="background:linear-gradient(160deg,#dcd6c4,#8fae5a 55%,#5a7a30)"></div>
  <h4>GREEN COFFEE</h4>
  <p>This is Pixelwright's version of Lorem Ipsum. Proin gravida nibh vel velit auctor aliquet.</p>
  <div class="more">Read More</div>
</article>

<div class="abs taste-strip"></div>
<section class="abs taste">
  <h2 class="abs script" style="top:90px;color:var(--white)">Start The Day</h2>
  <h2 class="abs script" style="top:162px;color:var(--gold-light)">With Great Taste</h2>
  <p class="abs">This is Pixelwright's version of Lorem Ipsum. Proin gravida nibh vel velit auctor aliquet. Aenean sollicitudin, lorem quis bibendum auctor, nisi elit consequat ipsum.</p>
</section>
<svg class="abs taste-notch" width="60" height="36" viewBox="0 0 60 36"><path d="M0 0 H60 L30 34 Z" fill="#b8925a"/></svg>

<section class="abs order" role="img" aria-label="Banner with a photograph of coffee beans behind the order text">
  <div class="abs order-icon"><svg width="44" height="44" viewBox="0 0 44 44"><path d="M12 6 L18 6 L21 14 L17 17 C19 22 22 25 27 27 L30 23 L38 26 L38 32 C38 35 35 38 32 38 C18 37 7 26 6 12 C6 9 9 6 12 6 Z" fill="#d2b27c"/></svg></div>
  <h3 class="abs">Order online</h3>
  <p class="abs">Hours: 8am - 11pm</p>
</section>

<footer class="abs footer">
  <div class="abs" style="left:128px;top:64px;width:320px">
    <h5>ABOUT US</h5>
    <p style="margin-top:18px">This is Pixelwright's version of Lorem Ipsum. Proin gravida nibh vel velit auctor aliquet. Aenean sollicitudin, lorem quis bibendum auctor, nisi elit consequat ipsum, nec sagittis sem nibh id elit. Duis sed odio sit amet nibh vulputate cursus.</p>
  </div>
  <div class="abs" style="left:505px;top:64px">
    <h5>NAVIGATION</h5>
    <ul class="foot-nav" style="margin-top:14px">
      <li>HOME</li><li>MENU</li><li>GALLERY</li><li>ABOUT</li><li>CONTACT US</li>
    </ul>
  </div>
  <div class="abs" style="left:706px;top:64px">
    <h5>GET IN TOUGH</h5>
    <ul class="social" style="margin-top:18px">
      <li>BREWBOOK</li><li>CHIRPLY</li><li>LINKWORKS</li>
    </ul>
  </div>
  <div class="abs" style="left:910px;top:64px"><h5>DAPPLE BREW</h5></div>
  <div class="abs foot-brand">Dapple Brew</div>
  <div class="abs foot-base"></div>
</footer>

</body>
</html>
```